IT Professional business card with a hometown feel and a little edgy.

My business name is Tamble Website Solutions. But I have ended up doing much more. I live in a very small remote community, where everyone knows everyone. We like the one-on-one customer service in this community. I do computer tutoring, virus removal, networking, and software training. My clients are businesses and private individuals.

My website is tamblewebsitesolutions.example, when I first designed it I was going for a fresh, clean look, which I still like. But I am thinking about making the website a bit more edgy to match my new logo from ArtHively (logo attached). At this time my website does not display the new logo, but I plan on redesigning the website in the future to match the logo and business card.

My tag line is "Put the web to work for you"

I'm thinking I would like to have the business card printed with a metallic finish.
Updates

Please do not use black backgrounds, or any solid dark colors. Prefer light or white backgrounds.

Target Market(s)

Small businesses. Individuals that need computer help at home.

Industry/Entity Type

It Company

Contact Information for Business Card

Nora Prandell
Tamble Website Solutions
PO Box 7153
Larkmoor, WA 98512
Cell: 555-271-3096
nora@tamblewebsitesolutions.example
tamblewebsitesolutions.example

Font styles to use
Serif

Requirements
Must have
• Must have all the information listed in "Business Card Details"
• Must use the logo provided.
• Use the colors from the provided logo
Nice to have
• Would like to use my tagline "Put the web to work for you" all lowercase

```html
<!DOCTYPE html>
<html lang="en">
<head>
<meta charset="utf-8">
<title>Tamble Website Solutions – Business Card</title>
<link rel="stylesheet" href="https://fonts.googleapis.com/css2?family=Open+Sans:wght@400;600&family=Roboto:wght@400;700&display=swap">
<style>
  :root {
    --backdrop: #e9e6e2;
    --metal-light: #f4f4f4;
    --metal-mid: #d9d9d9;
    --metal-dark: #b9b9b9;
    --brand-green: #1e7a35;
    --brand-brown: #4a3a30;
    --ink: #3b302a;
    --white: #ffffff;
  }
  * { box-sizing: border-box; margin: 0; padding: 0; }
  html, body { width: 1200px; height: 1000px; overflow: hidden; }
  body {
    background: var(--backdrop);
    position: relative;
    font-family: "Roboto", Arial, sans-serif;
    color: var(--ink);
  }
  .card {
    position: absolute;
    left: 265px;
    width: 667px;
    height: 397px;
    overflow: hidden;
    background:
      repeating-linear-gradient(0deg, rgba(255,255,255,0.12) 0 1px, rgba(0,0,0,0.03) 1px 3px),
      linear-gradient(100deg, var(--metal-dark) 0%, var(--metal-mid) 22%, var(--metal-light) 48%, var(--metal-mid) 70%, var(--metal-dark) 100%);
    box-shadow: 0 6px 14px rgba(0,0,0,0.25);
  }
  .card--front { top: 73px; }
  .card--back { top: 533px; }

  .wordmark {
    position: absolute;
    display: flex;
    align-items: center;
    gap: 18px;
    font-family: "Open Sans", Arial, sans-serif;
    font-weight: 400;
    color: var(--brand-green);
    line-height: 1.08;
  }
  .wordmark__square { background: var(--brand-green); flex: none; }
  .card--front .wordmark { left: 185px; top: 46px; font-size: 23px; }
  .card--front .wordmark__square { width: 52px; height: 52px; }
  .card--back .wordmark { left: 325px; top: 120px; font-size: 31px; }
  .card--back .wordmark__square { width: 72px; height: 72px; }

  .holder-name {
    position: absolute;
    left: 440px;
    top: 222px;
    width: 220px;
    text-align: center;
    font-weight: 700;
    font-size: 24px;
    color: var(--brand-green);
  }
  .contact {
    position: absolute;
    left: 33px;
    top: 248px;
    font-size: 16px;
    line-height: 24px;
  }
  .contact__row { display: flex; align-items: center; gap: 8px; }
  .contact__row svg { width: 13px; height: 13px; flex: none; }
  .contact__company { margin-top: 8px; font-weight: 700; font-size: 17px; }

  .band { position: absolute; left: 0; bottom: 0; width: 667px; }
  .website {
    position: absolute;
    right: 34px;
    bottom: 9px;
    font-size: 16px;
    color: var(--white);
  }
  .tagline {
    position: absolute;
    left: 0;
    width: 667px;
    bottom: 7px;
    text-align: center;
    font-size: 17px;
    letter-spacing: 1px;
    color: var(--white);
  }
</style>
</head>
<body>

<section class="card card--front" aria-label="Business card front">
  <div class="wordmark">
    <span class="wordmark__square"></span>
    <span>Tamble<br>Website<br>Solutions</span>
  </div>

  <p class="holder-name">Nora Prandell</p>

  <div class="contact">
    <div class="contact__row">
      <svg viewBox="0 0 13 13" aria-hidden="true"><rect x="3" y="0.5" width="7" height="12" rx="1.2" fill="none" stroke="#1e7a35" stroke-width="1.4"/><rect x="5" y="10" width="3" height="1" fill="#1e7a35"/></svg>
      <span>555-271-3096</span>
    </div>
    <div class="contact__row">
      <svg viewBox="0 0 13 13" aria-hidden="true"><rect x="0.5" y="2.5" width="12" height="8" fill="#1e7a35"/><path d="M0.5 2.5 L6.5 7 L12.5 2.5" fill="none" stroke="#ffffff" stroke-width="1"/></svg>
      <span>nora@tamblewebsitesolutions.example</span>
    </div>
    <p class="contact__company">Tamble Website Solutions</p>
    <p>PO Box 7153, Larkmoor, WA 98512</p>
  </div>

  <svg class="band" height="34" viewBox="0 0 667 34" aria-hidden="true">
    <rect x="0" y="15" width="360" height="19" fill="#4a3a30"/>
    <polygon points="350,0 667,0 667,34 335,34" fill="#1e7a35"/>
    <polygon points="350,0 356,0 341,34 335,34" fill="#ffffff" opacity="0.8"/>
  </svg>
  <p class="website">tamblewebsitesolutions.example</p>
</section>

<section class="card card--back" aria-label="Business card back">
  <div class="wordmark">
    <span class="wordmark__square"></span>
    <span>Tamble<br>Website<br>Solutions</span>
  </div>

  <svg class="band" height="32" viewBox="0 0 667 32" aria-hidden="true">
    <rect x="0" y="10" width="667" height="22" fill="#4a3a30"/>
    <polygon points="176,0 500,0 516,32 152,32" fill="#ffffff" opacity="0.85"/>
    <polygon points="180,0 496,0 510,30 158,30" fill="#1e7a35"/>
  </svg>
  <p class="tagline">Put the web to work for you</p>
</section>

</body>
</html>
```